Album art cover

Album art design concept, my band will be releasing a 11 song rock album in the next few Months. We will be using it as a CD cover, poster, online art cover, maybe even Vinyl. Working album titles are "Copper in the rain" (Preferred album title) or "A lantern under the tide". Anything abstract, painting-like design, or whatever type of design that comes to mind. Fonts are designers choice. Thank You

Target Market(s)

Music business

Colors

Designer to choose colors to be used in the design.

Requirements
Must have
• Our band logo
Nice to have
• Anything abstract, attractive painting type, maybe even some kind of a futuristic design.
Should not have
• Skulls, blood-like, scary designs, nudity, emo type of design

```html
<!DOCTYPE html>
<html lang="en">
<head>
<meta charset="utf-8">
<title>Copper in the rain — Tonic Vault</title>
<link href="https://fonts.googleapis.com/css2?family=Antonio:wght@100;700&display=swap" rel="stylesheet">
<style>
  :root {
    --ink-black: #000000;
    --paper-white: #ffffff;
    --silver-light: #f4f5f8;
    --silver-mid: #c9cbd2;
    --graphite: #2a2a2c;
  }
  html, body {
    margin: 0;
    padding: 0;
    width: 1200px;
    height: 1200px;
    overflow: hidden;
    background: var(--ink-black);
  }
  .cover {
    position: relative;
    width: 1200px;
    height: 1200px;
    background: var(--ink-black);
    font-family: "Antonio", "Arial Narrow", sans-serif;
    color: var(--paper-white);
  }
  .album-title {
    position: absolute;
    top: 209px;
    left: 0;
    width: 1200px;
    margin: 0;
    text-align: center;
    font-weight: 100;
    font-size: 42px;
    line-height: 1;
    letter-spacing: 0.27em;
    text-indent: 0.27em;
    text-transform: uppercase;
  }
  .cover-artwork {
    position: absolute;
    left: 395px;
    top: 371px;
    width: 434px;
    height: 447px;
    background:
      radial-gradient(ellipse 45% 55% at 48% 50%, var(--silver-light) 0%, rgba(220,222,228,0.9) 55%, rgba(255,255,255,0) 80%),
      linear-gradient(90deg, var(--paper-white) 0%, var(--silver-light) 35%, var(--silver-mid) 62%, var(--graphite) 100%);
  }
  .band-name {
    position: absolute;
    left: 458px;
    top: 952px;
    width: 307px;
    margin: 0;
    font-weight: 700;
    font-size: 44px;
    line-height: 45px;
    letter-spacing: 0.16em;
    text-transform: uppercase;
    color: var(--paper-white);
  }
  .band-name span {
    display: block;
  }
  .band-name .line-one {
    text-align: left;
  }
  .band-name .line-two {
    text-align: right;
    margin-right: -0.16em;
  }
</style>
</head>
<body>
  <main class="cover">
    <h1 class="album-title">Copper in the rain</h1>
    <div class="cover-artwork" role="img" aria-label="Album cover artwork in white, silver and graphite tones"></div>
    <p class="band-name"><span class="line-one">Tonic</span><span class="line-two">Vault</span></p>
  </main>
</body>
</html>
```